Lantern Vale Photography business card design required

Needing business card made up for my new photography business.

Target Market(s)

Target will mostly be regular people with the occasional industrial or commercial customer.

Industry/Entity Type

Business

Font styles to use
Sans Serif

Colors

Designer to choose colors to be used in the design.

Requirements
Must have
• Morgan Tillbrook
Ph: 0437 262 508
Email: info@lanternvalephoto.example
Web: www.lanternvalephoto.example

On the back possibly links for social media including Lensbook, Photoflow and Snapgrid (links to be determined).

```html
<!DOCTYPE html>
<html lang="en">
<head>
<meta charset="utf-8">
<title>Lantern Vale Photography – Business Card</title>
<link rel="stylesheet" href="https://fonts.googleapis.com/css2?family=Arimo:wght@400;700&display=swap">
<style>
  :root {
    --bg: #eeeeee;
    --card: #ffffff;
    --blue: #2a8fd4;
    --ink: #3b3b3b;
    --text: #2a2a2a;
  }
  html, body {
    margin: 0;
    width: 1200px;
    height: 908px;
    overflow: hidden;
    background: var(--bg);
    font-family: "Arimo", Arial, sans-serif;
  }
  .stage {
    position: relative;
    width: 1200px;
    height: 908px;
  }
  .card {
    position: absolute;
    display: block;
    background: var(--card);
    box-shadow: 0 6px 18px rgba(0,0,0,0.12);
  }
  .card--front { left: 70px; top: 150px; }
  .card--back  { left: 760px; top: 190px; }
  .rule { stroke: var(--blue); stroke-width: 3; }
  .mark-ring { fill: none; stroke: var(--blue); stroke-width: 7; }
  .brand { fill: var(--ink); font-weight: 700; font-family: "Arimo", Arial, sans-serif; }
  .name { font-weight: 700; font-size: 30px; letter-spacing: 0.5px; font-family: "Arimo", Arial, sans-serif; }
  .name-first { fill: var(--blue); }
  .name-last { fill: var(--ink); }
  .contact { fill: var(--text); font-size: 14px; font-family: "Arimo", Arial, sans-serif; }
</style>
</head>
<body>
<main class="stage">

  <!-- Front: contact side -->
  <svg class="card card--front" width="560" height="340" viewBox="0 0 560 340" aria-label="Business card front">
    <line class="rule" x1="150" y1="0" x2="150" y2="100"/>
    <circle class="mark-ring" cx="150" cy="160" r="48"/>
    <text class="brand" x="150" y="245" text-anchor="middle" font-size="24">Lantern Vale</text>
    <line class="rule" x1="150" y1="265" x2="150" y2="340"/>

    <text class="name" x="530" y="108" text-anchor="end"><tspan class="name-first">MORGAN</tspan> <tspan class="name-last">TILLBROOK</tspan></text>
    <line class="rule" x1="282" y1="120" x2="530" y2="120"/>

    <text class="contact" x="530" y="146" text-anchor="end">0437 262 508</text>
    <text class="contact" x="530" y="166" text-anchor="end">info@lanternvalephoto.example</text>
    <text class="contact" x="530" y="186" text-anchor="end">www.lanternvalephoto.example</text>

    <text class="contact" x="286" y="222">Lensbook</text>
    <text class="contact" x="286" y="242">Photoflow</text>
    <text class="contact" x="286" y="262">Snapgrid</text>
  </svg>

  <!-- Back: brand side -->
  <svg class="card card--back" width="330" height="540" viewBox="0 0 330 540" aria-label="Business card back">
    <line class="rule" x1="165" y1="0" x2="165" y2="150"/>
    <line class="rule" x1="270" y1="150" x2="330" y2="150"/>
    <circle class="mark-ring" cx="165" cy="250" r="62"/>
    <text class="brand" x="165" y="352" text-anchor="middle" font-size="28">Lantern Vale</text>
    <line class="rule" x1="0" y1="395" x2="60" y2="395"/>
    <line class="rule" x1="165" y1="380" x2="165" y2="540"/>
  </svg>

</main>
</body>
</html>
```